Riddle of the Ivory Owl

We are hosting an open-to-the-public murder mystery dinner and masquerade ball on Oct. 31. I need a postcard design that we can display, hand out and mail for marketing.

We produce events in the KC area.

I'd like to see designs with a Halloween masquerade ball/murder mystery theme.

Events

```html
<!DOCTYPE html>
<html lang="en">
<head>
<meta charset="utf-8">
<title>Murder Mystery Dinner &amp; Masquerade Ball – Postcard</title>
<link rel="stylesheet" href="https://fonts.googleapis.com/css2?family=Metal+Mania&family=Great+Vibes&family=Open+Sans:wght@700;800&family=Cabin:wght@400;700&display=swap">
<style>
  :root {
    --stage: #6b6b6b;
    --night: #1c0b1c;
    --night-deep: #120612;
    --plum: #4a1a45;
    --magenta: #c2438f;
    --pink: #e86aa8;
    --blood: #d9262e;
    --hot-pink: #e8177f;
    --ember: #f39a1e;
    --white: #ffffff;
    --mist: #c9c0cc;
    --lime: #7cc242;
  }
  * { margin: 0; padding: 0; box-sizing: border-box; }
  html, body { width: 1200px; height: 982px; overflow: hidden; background: var(--stage); }
  .canvas { position: relative; width: 1200px; height: 982px; }
  .postcard {
    position: absolute; left: 109px; top: 112px; width: 982px; height: 755px;
    overflow: hidden;
    background: radial-gradient(ellipse at 50% 30%, var(--plum) 0%, var(--night) 55%, var(--night-deep) 100%);
  }
  .art { position: absolute; display: block; }
  .art--swirl { left: 0; top: 0; width: 982px; height: 420px; }
  .art--skull { left: 230px; top: 300px; width: 540px; height: 455px; }
  .art--pumpkin { left: 860px; top: 370px; width: 130px; height: 135px; }
  .art--haunted { left: 770px; top: 500px; width: 212px; height: 255px; }

  .brand {
    position: absolute; left: 44px; top: 17px; width: 205px; height: 168px;
    display: flex; align-items: center; justify-content: center; gap: 10px;
  }
  .brand__dot { width: 16px; height: 16px; border-radius: 50%; background: var(--lime); flex: none; }
  .brand__name {
    font-family: "Cabin", sans-serif; font-weight: 700; font-size: 24px;
    color: var(--white); line-height: 1.1; text-align: left;
  }

  .date {
    position: absolute; left: 420px; top: 50px;
    font-family: "Open Sans", sans-serif; font-weight: 800; color: var(--white);
    display: flex; align-items: baseline; white-space: nowrap;
  }
  .date__day { font-size: 98px; letter-spacing: -2px; line-height: 1; }
  .date__suffix { font-size: 22px; font-weight: 700; align-self: flex-start; margin: 8px 8px 0 2px; }
  .date__month { font-size: 62px; letter-spacing: -2px; line-height: 1; }

  .title {
    position: absolute; text-align: center;
    font-family: "Metal Mania", fantasy; color: var(--white);
    text-transform: uppercase; line-height: 1; white-space: nowrap;
  }
  .title--line1 { left: 100px; top: 208px; width: 830px; font-size: 84px; letter-spacing: 11px; }
  .title--line2 { left: 380px; top: 302px; width: 310px; font-size: 70px; letter-spacing: 6px; }
  .script {
    position: absolute; font-family: "Great Vibes", cursive; color: var(--white);
    line-height: 1; white-space: nowrap;
  }
  .script--amp { left: 686px; top: 322px; font-size: 66px; }
  .script--ball { left: 96px; top: 372px; font-size: 126px; word-spacing: 30px; }

  .details {
    position: absolute; left: 27px; top: 568px;
    font-family: "Cabin", sans-serif; font-size: 20px; line-height: 38px;
    color: var(--mist);
  }
  .details strong { font-weight: 700; }
</style>
</head>
<body>
<div class="canvas">
  <section class="postcard">
    <svg class="art art--swirl" viewBox="0 0 982 420" role="img" aria-label="Sweeping pink dotted swirl pattern across the night sky">
      <defs>
        <linearGradient id="swirlTone" x1="0" y1="0" x2="1" y2="0">
          <stop offset="0" stop-color="#c2438f" stop-opacity="0.12"/>
          <stop offset="0.5" stop-color="#c2438f" stop-opacity="0.5"/>
          <stop offset="1" stop-color="#e86aa8" stop-opacity="0.7"/>
        </linearGradient>
        <filter id="swirlSoft" x="-10%" y="-20%" width="120%" height="140%"><feGaussianBlur stdDeviation="10"/></filter>
      </defs>
      <path d="M-20 30 C250 -30 620 -10 1000 30 L1000 360 C820 220 520 180 260 160 C130 150 40 120 -20 100 Z" fill="url(#swirlTone)" filter="url(#swirlSoft)"/>
    </svg>

    <svg class="art art--skull" viewBox="0 0 540 455" role="img" aria-label="Silver skull with dripping red blood splatter and orange flames">
      <defs>
        <radialGradient id="skullTone" cx="0.5" cy="0.45" r="0.5">
          <stop offset="0" stop-color="#e8177f" stop-opacity="0.95"/>
          <stop offset="0.4" stop-color="#d9262e" stop-opacity="0.85"/>
          <stop offset="0.75" stop-color="#8a1a3a" stop-opacity="0.4"/>
          <stop offset="1" stop-color="#1c0b1c" stop-opacity="0"/>
        </radialGradient>
      </defs>
      <ellipse cx="270" cy="210" rx="270" ry="245" fill="url(#skullTone)"/>
    </svg>

    <svg class="art art--pumpkin" viewBox="0 0 130 135" role="img" aria-label="Glowing jack-o'-lantern">
      <defs>
        <radialGradient id="pumpkinTone" cx="0.5" cy="0.5" r="0.5">
          <stop offset="0" stop-color="#f39a1e" stop-opacity="0.8"/>
          <stop offset="0.55" stop-color="#7a3a10" stop-opacity="0.5"/>
          <stop offset="1" stop-color="#120612" stop-opacity="0"/>
        </radialGradient>
      </defs>
      <ellipse cx="70" cy="66" rx="62" ry="62" fill="url(#pumpkinTone)"/>
    </svg>

    <svg class="art art--haunted" viewBox="0 0 212 255" role="img" aria-label="Crescent moon over a haunted house with lit windows">
      <defs>
        <radialGradient id="moonTone" cx="0.45" cy="0.3" r="0.55">
          <stop offset="0" stop-color="#f39a1e" stop-opacity="0.75"/>
          <stop offset="0.5" stop-color="#5a2a14" stop-opacity="0.45"/>
          <stop offset="1" stop-color="#050205" stop-opacity="0"/>
        </radialGradient>
        <linearGradient id="houseTone" x1="0" y1="0" x2="0" y2="1">
          <stop offset="0" stop-color="#050205" stop-opacity="0"/>
          <stop offset="0.55" stop-color="#050205" stop-opacity="0.7"/>
          <stop offset="1" stop-color="#050205" stop-opacity="0.95"/>
        </linearGradient>
      </defs>
      <rect width="212" height="255" fill="url(#moonTone)"/>
      <rect width="212" height="255" fill="url(#houseTone)"/>
    </svg>

    <div class="brand">
      <span class="brand__dot"></span>
      <span class="brand__name">Nightfall<br>Events KC</span>
    </div>

    <div class="date">
      <span class="date__day">31.</span><span class="date__suffix">TH</span><span class="date__month">October</span>
    </div>

    <h1 class="title title--line1">Murder Mystery</h1>
    <div class="title title--line2">Dinner</div>
    <div class="script script--amp">&amp;</div>
    <div class="script script--ball">Masquerade ball</div>

    <p class="details">
      <strong>Dinner &amp; ball will be held on</strong><br>
      <strong>the 31th of October</strong> at XXXX.<br>
      Please notify by xxxx xxxxx<br>
      xxxxxxxxxxxx&nbsp; xxxxxxxxxxxx
    </p>
  </section>
</div>
</body>
</html>
```